KESTREL Posters

We are a very large, international law firm. We seek a collection of posters (approximately 4) as part of a communications campaign about the upgrade of the firm’s computer systems from Deskora 5.1 to Deskora 6.4 (Mailvane, Scribo, Gridora and Pitchwell). The audience for the campaign is made up of lawyers, legal secretaries, paralegals and administrative staff. The corporate environment is high-powered professionals focused on delivering superior client service.
Comprehensive training programs will be made available to help users make the transition from Deskora 5.1 to Deskora 6.4. We anticipate it being easier for the users to successfully transition if they take advantage of the training opportunities. Training for secretaries is mandatory, but training for lawyers is optional.
The posters should be designed to send a positive message about the upgraded system and encourage lawyers and secretaries to take advantage of the training opportunities. We have a “logo/tagline” for this initiative (attached) and we would like the posters to relate to the tagline, “KESTREL: Gear for Every Task Ahead”.

Reason: Would like to make sure there is sufficient time for designers to receive and respond to my latest feedback.

Reason: Extending to allow for enough time to update after my last feedback.

Target Market(s)

Attorneys who are either technophobic or uninterested in computers and secretaries who are fearful of computers and change generally.

Industry/Entity Type

Communications

Requirements
Must have
• Positive message.
Excitement.
Professional Look and Feel.
Nice to have
• The posters should relate to the tagline “KESTREL: Gear for Every Task Ahead”. See the attached file for what this looks like. The poster does not need to specifically mention Deskora or Deskora 6.4 or technology.

Your slider seems prone to misinterpretation. To clarify, the following describes the style that illustrates what the poster should communicate:
Elegant/Bold 50/50
Playful/Serious 60/40
Traditional/Modern 50/50
Personable/Professional 30/70
Feminine/Masculine 50/50
Colorful/Conservative 30/70
Economical/Upmarket 20/80
Playful-Professional-Conservative-Upmarket are more heavily weighted.
Should not have
• The concept should not focus on “change” – change makes people anxious and one of our goals with this campaign is to reduce anxiety about the change to Deskora 6.4.
The concept should also avoid negative comparisons/images/references to our current suite of tools (Deskora 5.1).

```html
<!DOCTYPE html>
<html lang="en">
<head>
<meta charset="utf-8">
<title>KESTREL: Gear for Every Task Ahead</title>
<link rel="stylesheet" href="https://fonts.googleapis.com/css2?family=Oswald:wght@500;600&family=Ubuntu:ital,wght@0,400;0,500;1,400;1,700&display=swap">
<style>
  :root {
    --navy: #0f2440;
    --navy-deep: #0a1a30;
    --navy-mid: #16355e;
    --navy-soft: #1e4475;
    --photo-glow: #5f8fc8;
    --orange: #c0501c;
    --yellow: #f6b51d;
    --maroon: #6b0b0b;
    --ink: #1d1d1d;
    --logo-grey: #5e5f6e;
    --paper: #ffffff;
  }
  * { margin: 0; padding: 0; box-sizing: border-box; }
  html, body { width: 934px; height: 1200px; overflow: hidden; background: var(--paper); }
  .poster { position: relative; width: 934px; height: 1200px; overflow: hidden; background: var(--paper); font-family: "Ubuntu", sans-serif; }
  .shapes { position: absolute; inset: 0; width: 934px; height: 1200px; }

  .brand { position: absolute; left: 132px; top: 72px; display: flex; align-items: center; gap: 12px; }
  .brand-dot { width: 42px; height: 42px; border-radius: 50%; background: var(--navy); flex: none; }
  .brand-name { font-weight: 400; font-size: 40px; letter-spacing: 4px; color: var(--logo-grey); line-height: 1; }
  .brand-tagline { position: absolute; left: 212px; top: 112px; font-size: 19px; color: var(--navy); letter-spacing: 0.6px; }

  .headline { position: absolute; right: 72px; top: 584px; text-align: right; font-family: "Oswald", sans-serif; font-weight: 600; font-size: 64px; line-height: 1.0; color: var(--yellow); }
  .headline .lead { color: var(--orange); }

  .call { position: absolute; left: 154px; top: 994px; font-size: 16px; color: var(--ink); letter-spacing: 0.2px; }
  .blurb { position: absolute; left: 156px; top: 1040px; width: 510px; font-style: italic; font-size: 15px; line-height: 1.3; color: var(--navy-deep); }
  .web { position: absolute; left: 330px; top: 1095px; width: 290px; text-align: center; font-style: italic; font-weight: 700; font-size: 22px; color: var(--yellow); }
</style>
</head>
<body>
<main class="poster">
  <svg class="shapes" viewBox="0 0 778 1000" preserveAspectRatio="none">
    <defs>
      <radialGradient id="hero-glow" cx="0.55" cy="0.62" r="0.55">
        <stop offset="0" stop-color="var(--photo-glow)"/>
        <stop offset="0.35" stop-color="#2c5c96"/>
        <stop offset="1" stop-color="var(--navy-deep)"/>
      </radialGradient>
      <linearGradient id="tool-tone" x1="0" y1="0" x2="1" y2="1">
        <stop offset="0" stop-color="#d9dbde"/>
        <stop offset="0.55" stop-color="#8d9196"/>
        <stop offset="1" stop-color="#f2c21a"/>
      </linearGradient>
    </defs>

    <!-- accent stripes -->
    <polygon points="590,45 632,12 660,12 618,45" fill="var(--maroon)"/>
    <polygon points="668,125 718,82 740,82 690,125" fill="var(--orange)"/>
    <polygon points="600,228 690,150 712,150 622,228" fill="var(--yellow)"/>
    <polygon points="742,345 778,300 778,328 762,345" fill="var(--orange)"/>
    <polygon points="0,470 22,470 0,500" fill="var(--maroon)"/>
    <polygon points="0,500 120,500 80,555 0,555" fill="var(--yellow)"/>
    <polygon points="50,588 270,588 310,550 90,550" fill="var(--orange)"/>
    <polygon points="72,702 200,702 330,565 205,565" fill="var(--yellow)"/>
    <polygon points="188,662 245,662 300,605 243,605" fill="var(--orange)"/>

    <!-- hero photograph area -->
    <polygon class="hero-photo" role="img" aria-label="Photograph: a businessman drawing glowing gear outlines in the air"
      points="0,150 120,30 620,12 778,12 778,458 412,458 350,520 290,565 70,565 0,500" fill="url(#hero-glow)"/>

    <!-- diagonal navy bands across the hero -->
    <g class="hero-bands">
      <polygon points="0,150 120,30 560,22 0,470" fill="var(--navy)" opacity="0.55"/>
      <polygon points="0,470 0,300 300,60 420,60" fill="var(--navy-mid)" opacity="0.6"/>
      <polygon points="0,500 440,52 740,52 280,500" fill="var(--navy-deep)" opacity="0.35"/>
      <polygon points="70,565 420,215 500,215 160,565" fill="var(--navy)" opacity="0.7"/>
      <polygon points="160,565 460,265 520,265 230,565" fill="var(--navy-soft)" opacity="0.55"/>
      <polygon points="560,12 640,12 400,250 330,250" fill="var(--navy)" opacity="0.45"/>
      <polygon points="620,228 778,228 778,300 700,300" fill="var(--navy-deep)"/>
      <polygon points="640,350 778,350 778,458 530,458" fill="var(--navy)"/>
      <polygon points="680,125 778,125 778,160 650,160" fill="var(--navy-mid)" opacity="0.8"/>
    </g>

    <!-- logo band -->
    <polygon points="28,137 140,38 440,38 360,137" fill="var(--paper)"/>

    <!-- headline panel -->
    <polygon points="412,458 778,458 778,660 350,660 350,520" fill="var(--paper)"/>

    <!-- tool photograph -->
    <polygon class="tool-photo" role="img" aria-label="Photograph: aviation snips with yellow and blue handles"
      points="470,740 600,690 700,670 778,665 778,840 700,835 610,800 490,760" fill="url(#tool-tone)"/>

    <!-- footer bands -->
    <polygon points="310,1000 778,1000 778,885 460,885" fill="var(--maroon)"/>
    <polygon points="45,925 570,925 665,858 140,858" fill="var(--yellow)"/>
    <polygon points="210,955 490,955 580,905 280,905" fill="var(--orange)"/>
  </svg>

  <div class="brand">
    <span class="brand-dot"></span>
    <span class="brand-name">KESTREL</span>
  </div>
  <p class="brand-tagline">gear for every task ahead</p>

  <h1 class="headline"><span class="lead">Kestrel:</span><br>Gear for Every<br>Task Ahead</h1>

  <p class="call">CALL 800-555-0199 FOR MORE INFORMATION.</p>
  <p class="blurb">Training sessions for every team begin soon. Book your place today and get more from the tools you rely on.</p>
  <p class="web">www.KESTRELLEGAL.com</p>
</main>
</body>
</html>
```